Creating a Label for a new CBD Vape Line call "Brisq".

This will be a project that will create the first label design on a BRISQ Vape product that is being rolled out in Colorado. The vape line will cater to high concentration CBD Vape sold in disposable vape pens and replacement cartridge's. In the sea of vape pens we want our packaging to stand out with a bold, bright, clean, abstract design that will highlight the brand "BRISQ" in a font that stands out and is quickly recognized. The target demographic for this line is 18-29 years of age. The mock up of the brisq vape picture does not meet our marketing desire, I just wanted to show you the approximate shape and size of the label and that the font used for the label will be added to the actual pen. This pen will have 100% CBD, cut with all natural terpenes with no need for chemicals like PG or VG, not many on the market like that. I included several marketing logos that caught our eye with other type product, please look at those as examples but we are open to creativity.

Target Market(s)

18-29 year old

Industry/Entity Type

CBD and Vape

Font styles to use
Serif
Sans Serif

Requirements
Must have
• bold, colorful, fun, eye catching
Nice to have
• Several brand ideas presented to give the flavor of the marketing. The example font on the prototype is not 'cool enough' to use, we'd like that name BRISQ to look and feel briiiisq. :-)
Should not have
• old school, boring, dull colors, small font

```html
<!DOCTYPE html>
<html lang="en">
<head>
<meta charset="utf-8">
<title>Brisq Vape — Label Concepts</title>
<link href="https://fonts.googleapis.com/css2?family=Montserrat:ital,wght@0,900;1,900&family=Great+Vibes&family=Playfair+Display:ital,wght@1,700&display=swap" rel="stylesheet">
<style>
  :root {
    --page: #ffffff;
    --frame: #3a3a3a;
    --label-dark: #231f20;
    --ink-light: #ffffff;
    --product-dark: #2a2a27;
    --product-mid: #3e3d37;
  }
  * { box-sizing: border-box; margin: 0; padding: 0; }
  html, body { width: 1200px; height: 786px; overflow: hidden; background: var(--page); }
  .sheet {
    position: relative; width: 1200px; height: 786px;
    border: 1px solid var(--frame); background: var(--page);
  }
  .label {
    position: absolute; top: 43px; width: 346px; height: 693px;
    background: var(--label-dark); overflow: hidden;
  }
  .label--bold { left: 26px; }
  .label--script { left: 420px; }
  .label--serif { left: 826px; }

  .art { position: absolute; left: 0; width: 100%; }
  .art--swirl {
    top: 283px; bottom: 0;
    background: radial-gradient(ellipse 48% 30% at 45% 62%, #e2436b 0%, #f1a23a 30%, #3b8fd6 55%, #0b0b0b 80%), #0b0b0b;
  }
  .art--marble {
    top: 317px; height: 330px;
    background: linear-gradient(125deg, #ff4f9a 0%, #f15b6c 25%, #ff8a3c 45%, #e84aa8 62%, #6c6fe6 82%, #3fc6e8 100%);
  }
  .art--ink {
    top: 115px; height: 540px;
    background:
      radial-gradient(ellipse 45% 35% at 10% 45%, #2fd0d8 0%, transparent 70%),
      radial-gradient(ellipse 50% 30% at 20% 90%, #9fc43a 0%, transparent 70%),
      radial-gradient(ellipse 40% 30% at 85% 85%, #f4c51d 0%, transparent 70%),
      linear-gradient(160deg, #9a3a9a 0%, #e2304a 35%, #ff5a2a 55%, #f5981e 100%);
  }

  .wordmark { position: absolute; color: var(--ink-light); line-height: 1; }
  .wordmark .name, .wordmark .line { display: block; white-space: nowrap; }

  .wordmark--bold { left: 34px; top: 50px; font-family: "Montserrat", sans-serif; font-weight: 900; }
  .wordmark--bold .name { font-size: 82px; letter-spacing: 0; }
  .wordmark--bold .line { font-size: 44px; font-style: italic; margin-top: 2px; }

  .wordmark--script { left: 62px; top: 40px; font-family: "Great Vibes", cursive; font-weight: 400; }
  .wordmark--script .name { font-size: 112px; }
  .wordmark--script .line { font-size: 62px; margin-top: -22px; padding-left: 92px; }

  .wordmark--serif {
    left: 0; right: 0; top: 38px; text-align: center;
    font-family: "Playfair Display", serif; font-weight: 700; font-style: italic;
  }
  .wordmark--serif .name { font-size: 64px; letter-spacing: 4px; }
  .wordmark--serif .line { font-size: 58px; margin-top: 2px; padding-right: 8px; }

  .product {
    position: absolute; width: 66px;
    transform: translate(-50%, -50%);
    background: linear-gradient(90deg, var(--product-dark), var(--product-mid), var(--product-dark));
  }
  .label--bold .product { left: 176px; top: 431px; height: 502px; transform: translate(-50%, -50%) rotate(-28deg); }
  .label--script .product { left: 180px; top: 428px; height: 489px; transform: translate(-50%, -50%) rotate(-29deg); }
  .label--serif .product { left: 191px; top: 455px; height: 460px; transform: translate(-50%, -50%) rotate(-30deg); }
</style>
</head>
<body>
  <main class="sheet">
    <section class="label label--bold">
      <div class="art art--swirl" role="img" aria-label="Glossy rainbow paint swirl on black"></div>
      <h1 class="wordmark wordmark--bold"><span class="name">BRISQ</span><span class="line">Vape</span></h1>
      <div class="product" role="img" aria-label="Photo of the disposable vape pen"></div>
    </section>

    <section class="label label--script">
      <div class="art art--marble" role="img" aria-label="Pink, orange and blue liquid marble pattern"></div>
      <h2 class="wordmark wordmark--script"><span class="name">Brisq</span><span class="line">Vape</span></h2>
      <div class="product" role="img" aria-label="Photo of the disposable vape pen"></div>
    </section>

    <section class="label label--serif">
      <div class="art art--ink" role="img" aria-label="Alcohol ink wash in red, orange, teal and lime"></div>
      <h2 class="wordmark wordmark--serif"><span class="name">BRISQ</span><span class="line">vape</span></h2>
      <div class="product" role="img" aria-label="Photo of the disposable vape pen"></div>
    </section>
  </main>
</body>
</html>
```